**** Business card design for VoltaNode ****

For my ICT company VoltaNode I need I need a business card design.

We design, build and host web-applications and we have our own CMS product.

Some good examples are attached.

The information should be:
Joris Tielenburg
Managing director
E: j.tielenburg@voltanode-example.nl
M: +31(0)6 57218064
T: +31(0)40 7249305
W: www.voltanode-example.nl

Address:
Berend Vlootweg 27
5612 KT Eindhoven

Industry/Entity Type

Business

Requirements
Must have
• - Use logo (see attachments)
- Double sided
- Distinctive
Nice to have
• - Place for a statement on the back-side: "Designed with knowledge, built with passion"
- HTML code (or Wordpress)
- Dark (black or dark-gray) side
- Small simple images for telephone, e-mail en Url.
- QR code (only if not disturbing), not required, just an option

```html
<!DOCTYPE html>
<html lang="en">
<head>
<meta charset="utf-8">
<title>VoltaNode business card</title>
<link href="https://fonts.googleapis.com/css2?family=Michroma&display=swap" rel="stylesheet">
<style>
  :root {
    --backdrop: #5a4536;
    --card-dark: #0c0c0d;
    --card-dark-soft: #2a2b2e;
    --card-light: #ffffff;
    --brand-blue: #21a9d6;
    --brand-steel: #7f97a6;
    --text-grey: #6f7478;
    --text-soft: #8a8f93;
    --shadow: rgba(0, 0, 0, 0.45);
  }
  * { margin: 0; padding: 0; box-sizing: border-box; }
  html, body { width: 1200px; height: 900px; overflow: hidden; }
  body {
    background: var(--backdrop);
    font-family: "Michroma", "Helvetica Neue", Arial, sans-serif;
    position: relative;
  }
  .card {
    position: absolute;
    top: 338px;
    width: 516px;
    height: 287px;
    box-shadow: 8px 10px 18px var(--shadow);
    overflow: hidden;
  }
  /* Front side */
  .card--front {
    left: 55px;
    border-radius: 70px 0 70px 0;
    background: radial-gradient(ellipse 260px 200px at 190px 120px, var(--card-dark-soft), var(--card-dark) 75%);
  }
  .front__texture {
    position: absolute; inset: 0;
    background: linear-gradient(180deg, rgba(255,255,255,0.03), rgba(255,255,255,0));
  }
  .front__brand {
    position: absolute;
    left: 84px; top: 96px;
    display: flex; align-items: center; gap: 22px;
  }
  .brand-dot {
    width: 88px; height: 88px; border-radius: 50%;
    background: var(--brand-blue);
  }
  .front__name {
    font-size: 36px;
    color: var(--brand-steel);
    letter-spacing: 1px;
  }
  .front__web {
    position: absolute;
    left: 0; right: 0; top: 234px;
    text-align: center;
    padding-left: 10px;
    font-size: 12px;
    letter-spacing: 4px;
    text-transform: uppercase;
    color: var(--text-soft);
  }
  /* Back side */
  .card--back {
    left: 628px;
    border-radius: 0 70px 0 70px;
    background: var(--card-light);
    color: var(--text-grey);
    text-transform: uppercase;
  }
  .back__brand {
    position: absolute;
    left: 0; right: 0; top: 26px;
    display: flex; justify-content: center; align-items: center; gap: 10px;
    padding-right: 20px;
  }
  .back__brand .brand-dot { width: 44px; height: 44px; }
  .back__brand-name {
    font-size: 24px;
    color: var(--brand-steel);
    text-transform: none;
  }
  .back__person {
    position: absolute; left: 0; right: 0; top: 98px;
    text-align: center; padding-right: 20px;
  }
  .person__name { font-size: 16px; color: var(--brand-blue); letter-spacing: 1px; }
  .person__role { font-size: 10px; letter-spacing: 1px; margin-top: 4px; }
  .person__mobile { font-size: 12px; letter-spacing: 1.5px; margin-top: 1px; }
  .back__contact {
    position: absolute; left: 14px; top: 172px;
    font-size: 12px; letter-spacing: 1px;
  }
  .contact__row { display: flex; align-items: center; gap: 8px; height: 24px; }
  .contact__row--email { font-size: 7px; letter-spacing: 0.2px; }
  .contact__icon { width: 15px; height: 15px; flex: none; }
  .back__address {
    position: absolute; right: 16px; top: 152px;
    text-align: right; font-size: 11px; letter-spacing: 1px; line-height: 24px;
  }
  .address__label { color: var(--brand-blue); text-transform: none; font-size: 12px; }
  .back__web {
    position: absolute; left: 0; right: 0; top: 254px;
    text-align: center; padding-right: 20px;
    font-size: 13px; letter-spacing: 2px; color: var(--text-soft);
  }
</style>
</head>
<body>
  <section class="card card--front" aria-label="Card front">
    <div class="front__texture" role="img" aria-label="Dark patterned card surface"></div>
    <div class="front__brand">
      <span class="brand-dot"></span>
      <span class="front__name">VoltaNode</span>
    </div>
    <p class="front__web">www.voltanode-example.nl</p>
  </section>

  <section class="card card--back" aria-label="Card back">
    <div class="back__brand">
      <span class="brand-dot"></span>
      <span class="back__brand-name">VoltaNode</span>
    </div>
    <div class="back__person">
      <p class="person__name">Joris Tielenburg</p>
      <p class="person__role">Managing director</p>
      <p class="person__mobile">+31(0)6 57218064</p>
    </div>
    <div class="back__contact">
      <p class="contact__row">
        <svg class="contact__icon" viewBox="0 0 16 16" aria-hidden="true">
          <path d="M2 6c0-2 2-3 6-3s6 1 6 3l-3 1-1-2H6L5 7 2 6z M4 8h8l1 5H3z" fill="#21a9d6"/>
        </svg>
        +31(0)40 7249305
      </p>
      <p class="contact__row contact__row--email">
        <svg class="contact__icon" viewBox="0 0 16 16" aria-hidden="true">
          <circle cx="8" cy="8" r="7" fill="#21a9d6"/>
          <path d="M8 1v14M1 8h14M3 4c3 1.5 7 1.5 10 0M3 12c3-1.5 7-1.5 10 0" stroke="#fff" stroke-width="0.9" fill="none"/>
        </svg>
        j.tielenburg@voltanode-example.nl
      </p>
    </div>
    <div class="back__address">
      <p class="address__label">Address:</p>
      <p>Berend Vlootweg 27</p>
      <p>5612 KT Eindhoven</p>
    </div>
    <p class="back__web">www.voltanode-example.nl</p>
  </section>
</body>
</html>
```